Copper Gate Labradoodle web design

We're a new labradoodle breeder in Charleston, SC in need of a web design.

Our name is Copper Gate Labradoodles.

Site we like: http://www.fernhilldoodlery.example/
http://www.quailbrookpups.example/

Logo Font:
The ''Copper Gate'' font is called TestarossaNF and is available freely at http://www.typequarry.example/testarossa-nf.font.  The ''Labradoodles'' font is called Worstveld Sling Extra and is available freely at http://www.glyphbarn.example/WorstveldSlingExtra.php.

Requirements
Must have
• Our logo
1. Home page
2. Labradoodle F.A.Q.
3. Our doodles
4. Availability
5. Adoption Process
6. Contact us
Link/badge icon for Health Guarantee
Nice to have
• Color and font to match the logo.

An area to add pictures
Should not have
• Rainbows
Rainbow colors

```html
<!DOCTYPE html>
<html lang="en">
<head>
<meta charset="utf-8">
<title>Copper Gate Labradoodles</title>
<link rel="stylesheet" href="https://fonts.googleapis.com/css2?family=Archivo+Narrow&family=Fjalla+One&family=Italianno&display=swap">
<style>
  :root {
    --maroon: #650000;
    --deep: #320000;
    --pink: #ff6699;
    --rose: #e0557f;
    --white: #ffffff;
    --ink: #1a1a1a;
    --cream: #f7e8e8;
    --grass: #5c8a3a;
    --fur-gold: #c28a4c;
    --fur-brown: #6b4a33;
  }
  * { box-sizing: border-box; margin: 0; padding: 0; }
  html, body { width: 1000px; height: 1200px; overflow: hidden; background: var(--white); }
  .page { position: relative; width: 1000px; height: 1200px; font-family: "Archivo Narrow", "Arial Narrow", sans-serif; }

  .masthead { position: absolute; left: 0; top: 0; width: 1000px; height: 135px; background: var(--maroon); box-shadow: 0 4px 10px rgba(0,0,0,.35); z-index: 2; }
  .brand { position: absolute; left: 70px; top: 14px; width: 180px; height: 110px; display: flex; flex-direction: column; align-items: center; justify-content: flex-start; gap: 8px; z-index: 3; }
  .brand-mark { width: 56px; height: 56px; border-radius: 50%; background: var(--pink); }
  .brand-name { font-family: "Fjalla One", sans-serif; font-size: 17px; color: var(--cream); text-align: center; line-height: 1.15; }
  .main-nav { position: absolute; left: 272px; top: 100px; display: flex; gap: 11px; white-space: nowrap; }
  .main-nav a, .foot-nav a { font-family: "Fjalla One", sans-serif; font-variant: small-caps; text-decoration: none; letter-spacing: -0.3px; }
  .main-nav a { color: var(--white); font-size: 20px; text-shadow: 1px 1px 2px #000; }

  .social { position: absolute; display: flex; gap: 8px; }
  .social-item { display: flex; flex-direction: column; align-items: center; gap: 3px; }
  .social-square { width: 32px; height: 32px; background: var(--rose); }
  .social-label { font-family: "Fjalla One", sans-serif; font-size: 10px; }
  .masthead .social { right: 22px; top: 16px; }
  .masthead .social-label { color: var(--cream); }

  .gallery { position: absolute; left: 0; top: 0; width: 1000px; height: 583px; }
  .welcome-title, .section-title { position: absolute; font-family: "Italianno", cursive; font-weight: 400; line-height: 1; white-space: nowrap; }
  .welcome-title { left: 135px; top: 392px; font-size: 66px; color: var(--ink); }
  .copy { position: absolute; font-size: 12.5px; line-height: 16.7px; text-align: center; }
  .welcome-copy { left: 38px; top: 454px; width: 374px; color: var(--ink); }

  .cta { position: absolute; display: flex; align-items: center; justify-content: center; border-radius: 14px; font-family: "Italianno", cursive; line-height: 1; white-space: nowrap; color: var(--white); text-decoration: none;
    background: linear-gradient(180deg, #c4506f 0%, #7a1a2c 30%, #3a0008 60%, #2a0006 100%); box-shadow: 6px 8px 10px rgba(0,0,0,.45); }
  .cta-labradoodles { left: 527px; top: 438px; width: 306px; height: 82px; font-size: 42px; border: 4px solid #2a0006; }
  .cta-availability { left: 275px; top: 918px; width: 286px; height: 75px; font-size: 54px; }

  .adoption { position: absolute; left: 0; top: 583px; width: 1000px; height: 617px; background: var(--deep); }
  .adoption .section-title { left: 122px; top: 25px; font-size: 60px; color: var(--white); }
  .adoption-copy { left: 55px; top: 92px; width: 375px; color: var(--white); }
  .photo { position: absolute; }
  .photo-puppy { left: 516px; top: 30px; width: 218px; height: 163px; background: linear-gradient(160deg, var(--grass), #3f6a26 55%, #d2a06a 60%, #4e7a30); }
  .photo-trio { left: 638px; top: 150px; width: 273px; height: 189px; background: linear-gradient(135deg, var(--fur-gold), var(--fur-brown) 55%, #8a7a6a); }

  .site-footer { position: absolute; left: 97px; top: 1033px; width: 816px; height: 167px; background: var(--pink); }
  .foot-nav { position: absolute; left: 30px; top: 18px; display: flex; gap: 17px; white-space: nowrap; }
  .foot-nav a { color: var(--ink); font-size: 21px; }
  .site-footer .social { left: 666px; top: 22px; }
  .site-footer .social-square { background: var(--maroon); }
  .site-footer .social-label { color: var(--ink); }
</style>
</head>
<body>
<div class="page">

  <header class="masthead">
    <nav class="main-nav">
      <a href="#">Home</a><a href="#">Labradoodle FAQ</a><a href="#">Our Doodles</a><a href="#">Availability</a><a href="#">Adoption Process</a><a href="#">Contact Us</a>
    </nav>
    <div class="social">
      <div class="social-item"><span class="social-square"></span><span class="social-label">Pawbook</span></div>
      <div class="social-item"><span class="social-square"></span><span class="social-label">Chirper</span></div>
      <div class="social-item"><span class="social-square"></span><span class="social-label">Feedline</span></div>
    </div>
  </header>

  <div class="brand">
    <span class="brand-mark"></span>
    <span class="brand-name">Copper Gate<br>Labradoodles</span>
  </div>

  <section class="welcome">
    <svg class="gallery" viewBox="0 0 1000 583">
      <defs>
        <linearGradient id="fade" x1="0" y1="0" x2="0" y2="1">
          <stop offset="0" stop-color="#b9a8a0" stop-opacity=".55"/>
          <stop offset="1" stop-color="#ffffff" stop-opacity="0"/>
        </linearGradient>
        <linearGradient id="goldPup" x1="0" y1="0" x2="1" y2="1">
          <stop offset="0" stop-color="#3a2a1e"/><stop offset=".5" stop-color="#c98a4e"/><stop offset="1" stop-color="#9a6a3e"/>
        </linearGradient>
        <linearGradient id="trio" x1="0" y1="0" x2="1" y2="1">
          <stop offset="0" stop-color="#a89a8c"/><stop offset=".45" stop-color="#6b4a33"/><stop offset="1" stop-color="#4a3a30"/>
        </linearGradient>
        <linearGradient id="whiteDog" x1="0" y1="0" x2="1" y2="1">
          <stop offset="0" stop-color="#3b3530"/><stop offset=".4" stop-color="#e8e6e2"/><stop offset="1" stop-color="#a8a4a0"/>
        </linearGradient>
      </defs>
      <polygon points="235,333 383,330 383,450 235,470" fill="url(#fade)"/>
      <polygon points="383,368 578,348 578,480 383,500" fill="url(#fade)"/>
      <polygon points="579,380 826,355 826,540 579,565" fill="url(#fade)"/>
      <polygon points="235,178 383,193 383,330 235,333" fill="url(#goldPup)" role="img" aria-label="Photo of a golden labradoodle puppy lying down"/>
      <polygon points="383,165 578,181 578,348 383,368" fill="url(#trio)" role="img" aria-label="Photo of three labradoodles together outdoors"/>
      <polygon points="579,148 826,170 826,355 579,380" fill="url(#whiteDog)" role="img" aria-label="Photo of a white labradoodle sitting on carpet"/>
    </svg>

    <h1 class="welcome-title">Welcome</h1>
    <p class="copy welcome-copy">Lorem ipsum dolor sit amet, consectetuer adipiscing elit. Aenean commodo ligula eget dolor. Aenean massa. Cum sociis natoque penatibus et magnis dis parturient montes, nascetur ridiculus mus. Donec quam felis, ultricies nec, pellentesque eu, pretium quis, sem. Nulla consequat massa quis enim. Donec pede justo, fringilla vel, aliquet nec, vulputate eget, arcu.hendrerit id, lorem. Maecenas nec odio et ante tincidunt tempus.</p>
    <a class="cta cta-labradoodles" href="#">See Our Labradoodles</a>
  </section>

  <section class="adoption">
    <h2 class="section-title">Adoption Process</h2>
    <p class="copy adoption-copy">Lorem ipsum dolor sit amet, consectetuer adipiscing elit. Aenean commodo ligula eget dolor. Aenean massa. Cum sociis natoque penatibus et magnis dis parturient montes, nascetur ridiculus mus. Donec quam felis, ultricies nec, pellentesque eu, pretium quis, sem. Nulla consequat massa quis enim. Donec pede justo, fringilla vel, aliquet nec, vulputate eget, arcu. In enim justo, rhoncus ut, imperdiet a, venenatis vitae, justo. Nullam dictum felis eu pede mollis pretium. Integer tincidunt. Cras dapibus. Vivamus elementum semper nisi. Aenean vulputate eleifend tellus. Aenean leo ligula, porttitor eu, consequat vitae, eleifend ac, enim. Aliquam lorem ante, dapibus in, viverra quis, feugiat a, tellus. Phasellus viverra nulla ut metus varius laoreet. Quisque rutrum. Aenean imperdiet. Etiam ultricies nisi vel augue. Curabitur ullamcorper ultricies nisi. Nam eget dui. Etiam rhoncus. Maecenas tempus, tellus eget condimentum rhoncus, sem quam semper libero, sit amet adipiscing sem neque sed ipsum. Nam quam nunc, blandit vel, luctus pulvinar,</p>
    <div class="photo photo-puppy" role="img" aria-label="Photo of a golden labradoodle puppy standing on grass"></div>
    <div class="photo photo-trio" role="img" aria-label="Photo of three labradoodles close up on a patio"></div>
  </section>

  <a class="cta cta-availability" href="#">Availability</a>

  <footer class="site-footer">
    <nav class="foot-nav">
      <a href="#">Copyright</a><a href="#">Contact Us</a><a href="#">Home</a><a href="#">FAQ</a><a href="#">Availability</a><a href="#">Adoption Process</a><a href="#">Our Dooodles</a>
    </nav>
    <div class="social">
      <div class="social-item"><span class="social-square"></span><span class="social-label">Pawbook</span></div>
      <div class="social-item"><span class="social-square"></span><span class="social-label">Chirper</span></div>
      <div class="social-item"><span class="social-square"></span><span class="social-label">Feedline</span></div>
    </div>
  </footer>

</div>
</body>
</html>
```